Contemporary new French wine brand needs logo and series of label design

to design a new contemporary logo and series of labels for a new French wine brand. We hope to attract not just current French wine drinkers but new ones who may appreciate a less traditional and more modern style.
Updates

Reason: we are wanting to extend the project for a few days more to receive more submissions since we had fewer designs submitted than we were expecting, maybe because of the holidays.

Target Market(s)

people who follow the arts community (eg. music, theatre, visual/video arts, dance) --- all mature ages.

Industry/Entity Type

French Wine

Requirements
Must have
• a clear, memorable treatment for the name CLAVINE with accompanying logo.
Nice to have
• embossing, matte/gloss refinement, tasteful foil stamping, coated stock for the whites to help the integrity of the paper in and out of ice buckets. A combo of say, three types of fonts; a semi custom font for the brand name Clavine and maybe a script and one other.
Should not have
• not traditional French

```html
<!DOCTYPE html>
<html lang="fr">
<head>
<meta charset="utf-8">
<title>Clavine 2009 — Cabernet Franc</title>
<link rel="stylesheet" href="https://fonts.googleapis.com/css2?family=Cinzel:wght@400;500;600&family=Pinyon+Script&display=swap">
<style>
  :root {
    --backdrop: #2a2a2a;
    --paper-light: #f1efe0;
    --paper-mid: #e2e0d1;
    --paper-shade: #c5c4ba;
    --ink: #1c1a17;
    --vintage: #6b5a48;
    --gold: #9a6a3a;
    --script-grey: #6e6c66;
    --wine-red: #a0182a;
    --scene-sky: #e4e2d4;
    --scene-ink: #8d8a80;
  }
  * { margin: 0; padding: 0; box-sizing: border-box; }
  html, body {
    width: 946px;
    height: 1200px;
    overflow: hidden;
    background: var(--backdrop);
  }
  .label {
    position: absolute;
    left: 106px;
    top: 177px;
    width: 733px;
    height: 845px;
    background:
      radial-gradient(ellipse 45% 40% at 30% 62%, rgba(255,253,236,0.75), rgba(255,253,236,0) 70%),
      linear-gradient(90deg, var(--paper-mid) 0%, var(--paper-light) 30%, var(--paper-mid) 60%, var(--paper-shade) 100%);
    text-align: center;
    color: var(--ink);
  }
  .estate-scene {
    position: absolute;
    left: 34px;
    top: 114px;
    width: 699px;
    height: 182px;
    background: linear-gradient(180deg, var(--scene-sky) 0%, var(--scene-sky) 40%, var(--scene-ink) 100%);
    opacity: 0.55;
  }
  .brand-name {
    position: absolute;
    left: 0;
    right: 0;
    top: 318px;
    font-family: "Cinzel", serif;
    font-weight: 500;
    font-size: 80px;
    letter-spacing: 3px;
    line-height: 1;
  }
  .brand-name .initial { font-size: 100px; }
  .vintage {
    position: absolute;
    left: 0;
    right: 0;
    top: 440px;
    font-family: "Cinzel", serif;
    font-size: 38px;
    letter-spacing: 3px;
    color: var(--vintage);
  }
  .house-mark {
    position: absolute;
    left: 0;
    right: 0;
    top: 570px;
    font-family: "Cinzel", serif;
    font-weight: 500;
    font-size: 30px;
    letter-spacing: 4px;
    color: var(--gold);
  }
  .region {
    position: absolute;
    left: 0;
    right: 0;
    top: 688px;
    font-family: "Pinyon Script", cursive;
    font-size: 52px;
    color: var(--script-grey);
  }
  .grape {
    position: absolute;
    left: 0;
    right: 0;
    top: 764px;
    font-family: "Cinzel", serif;
    font-weight: 500;
    font-size: 32px;
    letter-spacing: 4px;
    color: var(--wine-red);
  }
</style>
</head>
<body>
  <main class="label">
    <div class="estate-scene" role="img" aria-label="Engraved sketch of a country estate house behind a fence, with trees and rolling hills"></div>
    <h1 class="brand-name"><span class="initial">C</span>LAVINE</h1>
    <p class="vintage">2009</p>
    <p class="house-mark">Clavine</p>
    <p class="region">Val de Loire</p>
    <p class="grape">Cabernet Franc</p>
  </main>
</body>
</html>
```